Real Estate Sales Brokerage

Design a modern and fresh looking standard size business card, incorporate our logo's color scheme and modern appearance with head shot photo on front side and incorporate our log on the back side

Target Market(s)

Residential Home sales

Industry/Entity Type

Real Estate Agent

Font styles to use
Sans Serif

Colors

Designer to choose colors to be used in the design.

Requirements
Must have
• fresh, modern, not too busy, incorporate head shot in front of the card, incorporate logo in front and back of the card. Use logo design scheme as appropriate.
Nice to have
• horizontal and vertical options to compare would be nice.

```html
<!DOCTYPE html>
<html lang="en">
<head>
<meta charset="utf-8">
<title>Hearthstone Ridge Realty – Business Card</title>
<link rel="stylesheet" href="https://fonts.googleapis.com/css2?family=Cinzel:wght@400&family=PT+Sans:wght@400&display=swap">
<style>
  :root {
    --page-bg: #e9e7e3;
    --card-black: #0e0e0e;
    --gold: #e9c420;
    --olive: #6e6a34;
    --white: #f4f4f4;
    --photo-top: #3c4f78;
    --photo-bottom: #1f2d52;
  }
  * { margin: 0; padding: 0; box-sizing: border-box; }
  html, body {
    width: 1200px; height: 900px; overflow: hidden;
    background: var(--page-bg);
  }
  .canvas {
    position: relative; width: 1200px; height: 900px;
    display: flex; align-items: center; justify-content: center; gap: 50px;
  }
  .card {
    position: relative; width: 525px; height: 300px;
    background: var(--card-black);
    overflow: hidden;
    box-shadow: 0 10px 28px rgba(0,0,0,.25);
  }

  /* Front */
  .headshot {
    position: absolute; left: 30px; top: 70px; width: 245px; height: 230px;
    background: linear-gradient(180deg, var(--photo-top), var(--photo-bottom));
    border-radius: 110px 110px 0 0;
  }
  .accent-band {
    position: absolute; left: 275px; right: 0; bottom: 0; height: 26px;
    background: var(--olive);
  }
  .details {
    position: absolute; left: 292px; top: 82px;
    font-family: "PT Sans", sans-serif; color: var(--white);
  }
  .agent-name {
    font-family: "Cinzel", serif; color: var(--gold);
    font-size: 20px; letter-spacing: .5px; line-height: 1;
  }
  .agent-title { font-size: 14px; margin-top: 4px; }
  .contact-list { list-style: none; margin-top: 14px; }
  .contact-list li {
    display: flex; align-items: center; gap: 7px;
    font-size: 15px; line-height: 21px;
  }
  .contact-list svg { width: 11px; height: 11px; fill: var(--gold); flex: none; }
  .address { font-size: 15px; line-height: 21px; margin-top: 6px; }

  /* Back */
  .brand-lockup {
    position: absolute; inset: 0;
    display: flex; align-items: center; justify-content: center; gap: 16px;
  }
  .brand-mark { width: 44px; height: 44px; background: var(--olive); }
  .brand-name {
    font-family: "PT Sans", sans-serif; color: var(--olive);
    font-size: 24px; line-height: 1.1; text-transform: uppercase; letter-spacing: .5px;
  }
</style>
</head>
<body>
<main class="canvas">

  <section class="card card-front">
    <div class="headshot" role="img" aria-label="Headshot photo of the agent in a blue suit and red tie"></div>
    <div class="accent-band"></div>
    <div class="details">
      <h1 class="agent-name">MARCUS ELLERY</h1>
      <p class="agent-title">Managing Director</p>
      <ul class="contact-list">
        <li>
          <svg viewBox="0 0 24 24" aria-hidden="true"><path d="M6.6 10.8a15.1 15.1 0 0 0 6.6 6.6l2.2-2.2c.3-.3.7-.4 1-.2 1.1.4 2.3.6 3.6.6.6 0 1 .4 1 1V20c0 .6-.4 1-1 1A17 17 0 0 1 3 4c0-.6.4-1 1-1h3.5c.6 0 1 .4 1 1 0 1.3.2 2.5.6 3.6.1.3 0 .7-.2 1z"/></svg>
          (055)987654321
        </li>
        <li>
          <svg viewBox="0 0 24 24" aria-hidden="true"><path d="M2 5h20v14H2z M2 5l10 8 10-8" /></svg>
          hello@hearthridge.com
        </li>
        <li>
          <svg viewBox="0 0 24 24" aria-hidden="true"><circle cx="12" cy="12" r="10"/></svg>
          www.hearthridge.com
        </li>
      </ul>
      <p class="address">88, Harbour Lane,<br>Westfield, 40210</p>
    </div>
  </section>

  <section class="card card-back">
    <div class="brand-lockup">
      <span class="brand-mark" aria-hidden="true"></span>
      <p class="brand-name">Hearthstone<br>Ridge<br>Realty</p>
    </div>
  </section>

</main>
</body>
</html>
```